Business Card Design Project

I require a business card with the following information on them for various different people;
name
m:
f:
e:
I have a logo already and will attached that. We are in the construction industry. I require something clean and simple but eye catching at the same time. You can use another colour with our logo if you like and you can style the logo as well if you wish. I am open.
Also it needs to be front and back design.
Industry/Entity Type
Construction
Requirements
Must have
- Logo, name, mobile, fax and email address.
Front and back design

```html
<!DOCTYPE html>
<html lang="en">
<head>
<meta charset="utf-8">
<title>Ridgefield Developments – Business Card</title>
<link rel="stylesheet" href="https://fonts.googleapis.com/css2?family=Quicksand:wght@400;500&display=swap">
<style>
  :root {
    --card-bg: #ffffff;
    --brand-green: #6cbf46;
    --brand-grey: #3d3d3f;
    --text-ink: #231f20;
  }
  html, body {
    margin: 0;
    padding: 0;
    overflow: hidden;
    background: var(--card-bg);
  }
  .card {
    position: relative;
    width: 1200px;
    height: 686px;
    overflow: hidden;
    background: var(--card-bg);
    font-family: "Quicksand", sans-serif;
    color: var(--text-ink);
  }
  .brand-square {
    position: absolute;
    left: 128px;
    top: 140px;
    width: 240px;
    height: 240px;
    background: var(--brand-green);
  }
  .brand-name {
    position: absolute;
    left: 489px;
    top: 118px;
    margin: 0;
    font-weight: 500;
    color: var(--brand-grey);
    line-height: 1;
  }
  .brand-name__primary {
    display: block;
    font-size: 108px;
    letter-spacing: -1px;
  }
  .brand-name__secondary {
    display: block;
    margin-top: 6px;
    margin-left: 48px;
    font-size: 58px;
    letter-spacing: 1px;
  }
  .person-name {
    position: absolute;
    left: 503px;
    top: 342px;
    margin: 0;
    font-size: 47px;
    font-weight: 400;
    line-height: 1;
    letter-spacing: 1px;
  }
  .contact {
    position: absolute;
    margin: 0;
    font-size: 43px;
    font-weight: 400;
    line-height: 1;
    letter-spacing: 0.5px;
  }
  .contact--mobile { left: 89px;  top: 445px; }
  .contact--fax    { left: 741px; top: 445px; }
  .contact--email  { left: 0; right: 0; top: 546px; text-align: center; }
</style>
</head>
<body>
  <main class="card">
    <div class="brand-square" aria-hidden="true"></div>
    <h1 class="brand-name">
      <span class="brand-name__primary">Ridgefield</span>
      <span class="brand-name__secondary">DEVELOPMENTS</span>
    </h1>
    <p class="person-name">name name name name</p>
    <p class="contact contact--mobile">mobile: 123 456 6789</p>
    <p class="contact contact--fax">fax: 123 456 6789</p>
    <p class="contact contact--email">namename@example.com</p>
  </main>
</body>
</html>
```